Store Fixture business needs a buisness card design

We are looking for a business card design for a store fixture company. "KL Shelf Outfitters" we help small businesses with their start up by providing fixtures required to display their products.
It should have a simple yet innovative design in the front, and a refined look to our company.
We would like our logo, to have one of our products "display cases, clothing rack, mannequins" integrated in the design. And the rest of it just a clean look, which gives our address, store hours, and contact number, etc.
The color scheme as seen in the samples can be changed as long as the goal is achieved.
Industry/Entity Type
Business
Contact Information for Business Card
KL Shelf Outfitters
4362 Marlow Ave.
San Antonio,TX 78299
www.klshelfoutfitters.example
klpo@klshelfoutfitter.example
(210) 555-0188
M-F: 9-6pm
Sat: 10-3pm

```html
<!DOCTYPE html>
<html lang="en">
<head>
<meta charset="utf-8">
<title>KL Shelf Outfitters – Business Card</title>
<link href="https://fonts.googleapis.com/css2?family=Open+Sans:wght@400;600;700&display=swap" rel="stylesheet">
<style>
  :root {
    --stage: #1a1a1a;
    --card-white: #ffffff;
    --gold-light: #e6b224;
    --gold-mid: #d9a22a;
    --gold-deep: #cf8e2c;
    --gold-text: #e8a418;
    --ink: #4a4a4a;
    --ink-soft: #555555;
    --mark-faint: rgba(176, 110, 30, 0.5);
  }
  * { margin: 0; padding: 0; box-sizing: border-box; }
  html, body { width: 1200px; height: 900px; overflow: hidden; }
  body {
    background: var(--stage);
    font-family: "Open Sans", Arial, sans-serif;
    position: relative;
  }
  .card {
    position: absolute;
    top: 170px;
    width: 347px;
    height: 560px;
    overflow: hidden;
  }

  /* Front */
  .card-front { left: 259px; background: var(--card-white); }
  .tab {
    position: absolute;
    left: 102px;
    width: 143px;
    background: linear-gradient(180deg, var(--gold-light), var(--gold-deep));
  }
  .tab-top { top: 0; height: 30px; }
  .tab-bottom { bottom: 0; height: 27px; }

  .brand {
    position: absolute;
    top: 112px;
    left: 30px;
    display: flex;
    align-items: center;
    gap: 12px;
  }
  .brand-square {
    flex: none;
    width: 90px;
    height: 90px;
    background: linear-gradient(180deg, var(--gold-light), var(--gold-deep));
  }
  .brand-name {
    font-weight: 700;
    font-size: 23px;
    line-height: 1.2;
    letter-spacing: 1.5px;
    text-transform: uppercase;
    color: var(--ink);
  }

  .contact {
    position: absolute;
    top: 245px;
    left: 0;
    right: 0;
    list-style: none;
    font-size: 15px;
    color: var(--ink-soft);
  }
  .contact li {
    height: 23.5px;
    display: flex;
    justify-content: center;
    align-items: center;
    gap: 8px;
  }
  .contact svg { width: 12px; height: 12px; fill: var(--gold-text); flex: none; }

  .address {
    position: absolute;
    top: 336px;
    left: 0; right: 0;
    text-align: center;
    font-size: 15px;
    line-height: 23px;
    color: var(--ink-soft);
    font-style: normal;
  }
  .hours {
    position: absolute;
    top: 413px;
    left: 0; right: 0;
    text-align: center;
    color: var(--ink-soft);
    font-size: 15px;
  }
  .hours-title {
    font-weight: 600;
    font-size: 16.5px;
    color: var(--gold-text);
    margin-bottom: 2px;
  }

  /* Back */
  .card-back {
    left: 631px;
    background: linear-gradient(180deg, var(--gold-light) 0%, var(--gold-mid) 50%, var(--gold-deep) 100%);
  }
  .back-name {
    position: absolute;
    top: 58px;
    left: 20px;
    right: 20px;
    text-align: center;
    font-weight: 700;
    font-size: 46px;
    line-height: 1.15;
    letter-spacing: 1px;
    text-transform: uppercase;
    color: var(--mark-faint);
  }
  .product {
    position: absolute;
    border-radius: 2px;
    box-shadow: 0 2px 6px rgba(120, 70, 10, 0.25);
  }
  .product-wall-case {
    left: 39px; top: 272px; width: 89px; height: 120px;
    background: linear-gradient(180deg, #c44a2c 0%, #a52f1c 70%, #8a3a22 100%);
  }
  .product-rack {
    left: 147px; top: 277px; width: 92px; height: 113px;
    background: radial-gradient(ellipse at center, rgba(235,235,235,0.45), rgba(200,200,200,0.15) 75%);
    box-shadow: none;
  }
  .product-form {
    left: 259px; top: 268px; width: 60px; height: 222px;
    border-radius: 30px 30px 6px 6px;
    background: linear-gradient(180deg, #f3efe6 0%, #ede6d6 45%, #d8ac74 65%, #d9a46a 100%);
    box-shadow: none;
  }
  .product-counter-case {
    left: 49px; top: 415px; width: 154px; height: 105px;
    background: linear-gradient(180deg, #eef2f3 0%, #d4dcdf 78%, #9a4a2a 86%, #6e2f1a 100%);
  }
</style>
</head>
<body>
  <section class="card card-front" aria-label="Business card front">
    <div class="tab tab-top"></div>

    <div class="brand">
      <span class="brand-square" aria-hidden="true"></span>
      <span class="brand-name">KL Shelf<br>Outfitters</span>
    </div>

    <ul class="contact">
      <li>
        <svg viewBox="0 0 24 24" aria-hidden="true"><path d="M6.6 10.8a15.1 15.1 0 0 0 6.6 6.6l2.2-2.2a1 1 0 0 1 1-.25 11.4 11.4 0 0 0 3.6.57 1 1 0 0 1 1 1V20a1 1 0 0 1-1 1A17 17 0 0 1 3 4a1 1 0 0 1 1-1h3.5a1 1 0 0 1 1 1c0 1.25.2 2.45.57 3.6a1 1 0 0 1-.25 1z"/></svg>
        (210) 555-0188
      </li>
      <li>
        <svg viewBox="0 0 24 24" aria-hidden="true"><path d="M2 5h20v14H2z"/><path d="M3 6l9 7 9-7" fill="none" stroke="#fff" stroke-width="1.5"/></svg>
        klpo@klshelfoutfitter.example
      </li>
      <li>
        <svg viewBox="0 0 24 24" aria-hidden="true"><circle cx="12" cy="12" r="10"/><path d="M2 12h20M12 2c3 3 3 17 0 20M12 2c-3 3-3 17 0 20" fill="none" stroke="#fff" stroke-width="1.3"/></svg>
        www.klshelfoutfitters.example
      </li>
    </ul>

    <address class="address">4362 Marlow Ave.<br>San Antonio,TX 78299</address>

    <div class="hours">
      <p class="hours-title">Store Timings</p>
      <p>M-F: 9-6pm &nbsp;|&nbsp; Sat: 10-3pm</p>
    </div>

    <div class="tab tab-bottom"></div>
  </section>

  <section class="card card-back" aria-label="Business card back">
    <p class="back-name">KL Shelf<br>Outfitters</p>
    <div class="product product-wall-case" role="img" aria-label="Photo of a wood and glass wall display case"></div>
    <div class="product product-rack" role="img" aria-label="Photo of a chrome rolling clothing rack"></div>
    <div class="product product-form" role="img" aria-label="Photo of a dress form on a wooden tripod stand"></div>
    <div class="product product-counter-case" role="img" aria-label="Photo of a glass counter showcase"></div>
  </section>
</body>
</html>
```